Redesign of a growing event production company in atlanta!

www.vorquinstage.com - it's Wix.com site and I'd like to keep it within WIX if possible.
We purchased a new logo and we are looking for a redesign.
We specialize in many different aspects of the event production industry and we want our page to be better segmented, with separation between the audio video lighting and wedding services offered.
We also want this cleaned up, showcasing client feedback and highlighted photos. Our industry is very visual and we want some of our work showcased as well as area for event videos.
We want the ability to add new photos and videos as well as links to our blog. If we can incorporate our blog into the site, that would be great as well.
Attached is the new logo, we are going to have it animated and placed on the site as well. We love the color spectrum of light and the significance to event production. We would like the page to incorporate that.
Updates

There are just a few days left, please submit your final versions, with requested revisions.

Target Market(s)

Women are the main purchasees of our services. brides between 20 - 40, and then corporate event planners...we have a high end market. We are marketing to the people who plan galas and society socials.

Industry/Entity Type

It Company

Number of Pages Required

5+ page

Font styles to use
Sans Serif
Script

Requirements
Must have
• incorporate the same content I currently have on my site.
• A clear but fluid separation between our event production services (Audio Visual) and the wedding services we offer. We MUST also be able to clearly show what we do. We are a one stop show and we want to convey that.
Nice to have
• Color palette based off logo attached

```html
<!DOCTYPE html>
<html lang="en">
<head>
<meta charset="utf-8">
<title>Vorquin Events</title>
<link href="https://fonts.googleapis.com/css2?family=Oswald:wght@500;700&family=Open+Sans:ital,wght@0,400;0,600;0,700;1,400&family=PT+Sans:wght@400;700&display=swap" rel="stylesheet">
<style>
:root{
  --black:#0b0b0b;
  --nav-active:#5c1140;
  --plum:#6d0f4a;
  --teal:#0d4258;
  --white:#ffffff;
  --paper:#f3f3f3;
  --ink:#222222;
  --link-blue:#1d5f86;
  --red:#c7201e;
}
*{box-sizing:border-box;margin:0;padding:0}
html,body{width:694px;height:1200px;overflow:hidden;background:var(--black)}
body{position:relative;font-family:"Open Sans",Arial,sans-serif;color:var(--ink)}
.abs{position:absolute}

/* navigation */
.main-nav{left:0;top:0;width:694px;height:32px;background:var(--black);display:flex;justify-content:center;border-bottom:1px solid #2a2a2a}
.main-nav a{font-family:"Oswald",Impact,sans-serif;font-weight:500;font-size:10.5px;color:var(--white);text-decoration:none;text-transform:uppercase;padding:0 16.5px;line-height:32px;border-right:1px solid #262626}
.main-nav a:first-child{border-left:1px solid #262626}
.main-nav a.is-active{background:var(--nav-active)}

/* hero */
.hero{left:0;top:32px;width:694px;height:472px;background:linear-gradient(180deg,#a86e47 0%,#8b5535 18%,#6a3a22 45%,#3a1c0f 66%,#050505 88%,#000 100%)}
.brand{left:0;top:42px;width:694px;display:flex;justify-content:center;align-items:center;gap:8px}
.brand-dot{width:38px;height:38px;border-radius:50%;background:#1b1b1b}
.brand-name{font-family:"PT Sans",sans-serif;font-weight:400;font-size:24px;color:#1b1b1b;letter-spacing:.5px}
.slider{left:87px;top:127px;width:521px;height:211px;border:2px solid var(--white)}
.slider-photo{width:100%;height:100%;background:linear-gradient(180deg,#e8dccb 0%,#b39a7e 35%,#5a3b26 70%,#2b1a10 100%)}
.slider-caption{left:12px;bottom:8px;font-family:"Oswald",Impact,sans-serif;font-weight:700;font-size:16px;color:var(--white)}
.slider-dots{right:14px;bottom:12px;display:flex;gap:3px}
.slider-dots i{width:5px;height:5px;border-radius:50%;background:#888}
.slider-dots i.on{background:#ddd}
.arrow-btn{width:25px;height:25px;border-radius:50%;background:rgba(255,255,255,.25)}
.welcome-title{left:0;top:362px;width:694px;text-align:center;font-family:"PT Sans",sans-serif;font-weight:400;font-size:21px;color:var(--white)}
.welcome-title::before,.welcome-title::after{content:"";display:inline-block;width:60px;height:1px;background:#c9b49a;vertical-align:middle;margin:0 10px}
.welcome-text{left:98px;top:391px;width:498px;text-align:center;font-size:8.6px;line-height:13.6px;color:#f1f1f1}

/* services band */
.services-band{left:0;top:504px;width:694px;height:265px;background:linear-gradient(180deg,#7a4529,#9a5d38 50%,#6b3b22)}
.service-card{top:547px;width:238px;height:181px;background:var(--white)}
.service-card .ribbon{position:absolute;left:-4px;top:17px;width:246px;height:22px;color:var(--white);font-family:"Oswald",Impact,sans-serif;font-weight:700;font-size:12px;text-align:center;line-height:22px}
.service-card .media{position:absolute;left:3px;top:40px;width:232px;height:84px}
.service-card .play{position:absolute;left:100px;top:26px}
.service-card p{position:absolute;left:6px;top:128px;width:226px;text-align:center;font-size:7.6px;line-height:11px;color:var(--ink)}
.service-card .more{position:absolute;left:0;top:155px;width:100%;text-align:center;font-family:"PT Sans",sans-serif;font-weight:700;font-size:11px}
.service-card .more::before,.service-card .more::after{content:"";display:inline-block;width:30px;height:1px;background:currentColor;vertical-align:middle;margin:0 8px}
.service-card .base{position:absolute;left:0;bottom:0;width:100%;height:3px}
.card-wedding .ribbon,.card-wedding .base{background:var(--plum)}
.card-wedding .more{color:var(--plum)}
.card-wedding .media{background:linear-gradient(135deg,#6a8a4a,#c9c3b6 55%,#7a7a6a)}
.card-av .ribbon,.card-av .base{background:var(--teal)}
.card-av .more{color:var(--teal)}
.card-av .media{background:linear-gradient(180deg,#6a4a7a,#2a2234 55%,#15121a)}

/* blog */
.blog-section{left:0;top:769px;width:694px;height:195px;background:var(--paper)}
.blog-title{left:95px;top:797px;width:350px;text-align:center;font-family:"PT Sans",sans-serif;font-weight:400;font-size:19px;color:var(--ink)}
.blog-rule{left:95px;top:823px;width:350px;height:1px;background:#d4d4d4}
.blog-divider{left:268px;top:838px;width:1px;height:86px;background:#d8d8d8}
.blog-post{width:170px;display:flex;gap:7px}
.blog-post .thumb{width:22px;height:22px;flex:none;background:linear-gradient(135deg,#9a8a7a,#4a3f36)}
.blog-post h4{font-size:7.8px;font-weight:700;line-height:10px;color:var(--ink)}
.blog-post p{font-size:7.4px;line-height:10px;color:#333}
.blog-post time{display:block;font-size:7px;font-style:italic;font-weight:700;line-height:10px;color:var(--link-blue)}
.services-box{left:459px;top:799px;width:145px;height:137px;border-radius:5px;background:linear-gradient(180deg,#8a4e2c,#6a3a20);border:1px solid #4a2412}
.services-box h3{position:absolute;left:10px;top:8px;font-family:"PT Sans",sans-serif;font-weight:400;font-size:14px;color:var(--white)}
.services-box ul{position:absolute;left:12px;top:33px;list-style:none}
.services-box li{font-family:"Oswald",Impact,sans-serif;font-weight:500;font-size:8px;color:var(--white);height:18.5px;display:flex;align-items:center;gap:6px;text-transform:uppercase}
.services-box li::before{content:"";width:8px;height:6px;background:#e9ddd0;border-radius:1px}

/* events */
.events-section{left:0;top:964px;width:694px;height:175px;background:linear-gradient(180deg,#6a3a20,#8e5431 45%,#5e3219)}
.events-title{left:0;top:982px;width:694px;text-align:center;font-family:"Oswald",Impact,sans-serif;font-weight:700;font-size:18px;color:var(--white)}
.events-rule{left:95px;top:1011px;width:504px;height:1px;background:rgba(255,255,255,.3)}
.event{top:1024px;width:152px}
.event .cal{position:absolute;left:0;top:0;width:26px;height:26px;background:var(--white);border-radius:2px;overflow:hidden}
.event .cal::before{content:"";position:absolute;left:0;top:0;width:100%;height:6px;background:var(--red)}
.event .cal span{position:absolute;left:0;top:6px;width:100%;text-align:center;font-weight:700;font-size:13px;line-height:19px;color:#222}
.event h4{position:absolute;left:34px;top:2px;font-family:"PT Sans",sans-serif;font-weight:400;font-size:12px;color:#111;white-space:nowrap;text-transform:uppercase}
.event .month{position:absolute;left:34px;top:18px;font-size:5.5px;color:#222}
.event p{position:absolute;left:0;top:32px;width:152px;font-size:8px;font-style:italic;font-weight:400;line-height:10.5px;color:var(--white)}
.event .btn{position:absolute;left:0;top:70px;width:57px;height:20px;background:#111;border-radius:2px;color:var(--white);font-size:7.5px;text-align:center;line-height:20px}
.event .btn.is-hot{background:var(--red)}

/* footer */
.site-footer{left:0;top:1139px;width:694px;height:61px;background:linear-gradient(180deg,#1a1a1a,#050505)}
.social{left:311px;top:1156px;display:flex;gap:5px}
.social i{width:14px;height:14px;border-radius:50%;border:1px solid #bbb}
.copyright{left:0;top:1177px;width:694px;text-align:center;font-size:6.5px;color:#999}
.copyright b{color:var(--white)}
</style>
</head>
<body>
<nav class="main-nav abs">
  <a href="#" class="is-active">Get Inspired</a><a href="#">Services Offered</a><a href="#">Vorquin Owners</a><a href="#">Client Referrals</a><a href="#">Blog</a><a href="#">Contact Us</a>
</nav>

<section class="hero abs"></section>
<div class="brand abs"><span class="brand-dot"></span><span class="brand-name">VorquinEvents</span></div>

<div class="arrow-btn abs" style="left:54px;top:218px"><svg width="25" height="25"><path d="M14 7l-6 5.5 6 5.5" stroke="#fff" stroke-width="1.6" fill="none"/></svg></div>
<div class="arrow-btn abs" style="left:614px;top:218px"><svg width="25" height="25"><path d="M11 7l6 5.5-6 5.5" stroke="#fff" stroke-width="1.6" fill="none"/></svg></div>
<div class="slider abs">
  <div class="slider-photo" role="img" aria-label="Wedding couple's first dance in a columned ballroom surrounded by guests"></div>
  <div class="slider-caption abs">We provide quality, custom solutions for events</div>
  <div class="slider-dots abs"><i></i><i class="on"></i><i></i><i></i></div>
</div>

<h1 class="welcome-title abs">Welcome to VorquinEvents</h1>
<p class="welcome-text abs">Vorquin Events is an award winning event production company providing quality, custom event solutions catered to your specific needs from planning and entertainment to audio, video and lighting. Vorquin Stage Production's team has diverse professional experience working in professional Entertainment, Catering, Audio/Video Production, Venue Management and Lighting Production. This seperates us from our competition, giving you the best event experience! Mes cuml dia sed in lacus ut eniascet etor ingerto aliiqt es sitet amet eismod ictorut dolore ligulate ameti dapi licdu nt mtsent lusto dolor ltisim comme. Mes cuml dia sed inertio lacus ut eniascet ingerto aliiqt sit eism odictor. Ut ligulate ameti dapibus ticdu.</p>

<section class="services-band abs"></section>
<article class="service-card card-wedding abs" style="left:96px">
  <h3 class="ribbon">Wedding Services</h3>
  <div class="media" role="img" aria-label="Bride and groom posing outdoors among green trees">
    <svg class="play" width="32" height="32"><circle cx="16" cy="16" r="15" fill="rgba(255,255,255,.35)" stroke="#fff" stroke-width="1.5"/><path d="M12 9l11 7-11 7z" fill="#fff"/></svg>
  </div>
  <p>Dolor nunc vule putateulr ips dol consem donec semp ertet laciniate ultricie upien disse cmete dolo lecunc vule puta</p>
  <div class="more">more</div>
  <span class="base"></span>
</article>
<article class="service-card card-av abs" style="left:361px">
  <h3 class="ribbon">Audio Video Lighting</h3>
  <div class="media" role="img" aria-label="Production control room with screens and mixing desk">
    <svg class="play" width="32" height="32"><circle cx="16" cy="16" r="15" fill="rgba(255,255,255,.35)" stroke="#fff" stroke-width="1.5"/><path d="M12 9l11 7-11 7z" fill="#fff"/></svg>
  </div>
  <p>Dolor nunc vule putateulr ips dol consem donec semp ertet laciniate ultricie upien disse cmete dolo lecunc vule puta</p>
  <div class="more">more</div>
  <span class="base"></span>
</article>

<section class="blog-section abs"></section>
<svg class="abs" style="left:95px;top:800px" width="16" height="16"><circle cx="8" cy="8" r="7" fill="none" stroke="#999" stroke-width="1.3"/><path d="M9.5 5L6.5 8l3 3" stroke="#999" stroke-width="1.3" fill="none"/></svg>
<svg class="abs" style="left:427px;top:800px" width="16" height="16"><circle cx="8" cy="8" r="7" fill="none" stroke="#666" stroke-width="1.3"/><path d="M6.5 5l3 3-3 3" stroke="#666" stroke-width="1.3" fill="none"/></svg>
<h2 class="blog-title abs">OUR BLOG</h2>
<div class="blog-rule abs"></div>
<div class="blog-divider abs"></div>
<div class="blog-post abs" style="left:95px;top:838px"><div class="thumb" role="img" aria-label="Author portrait"></div><div><h4>Dolor nunc vulputateulr ips consec.</h4><p>Dodfh dnec semp efhrtet lacin iate.</p><time>- 31 March, 2015</time></div></div>
<div class="blog-post abs" style="left:282px;top:838px"><div class="thumb" role="img" aria-label="Author portrait"></div><div><h4>Dolor nunc vulputateulr ips consec.</h4><p>Dodfh dnec semp efhrtet lacin iate.</p><time>- 30 March, 2015</time></div></div>
<div class="blog-post abs" style="left:95px;top:893px"><div class="thumb" role="img" aria-label="Author portrait"></div><div><h4>Dolor nunc vulputateulr ips consec.</h4><p>Dodfh dnec semp efhrtet lacin iate.</p><time>- 25 March, 2015</time></div></div>
<div class="blog-post abs" style="left:282px;top:893px"><div class="thumb" role="img" aria-label="Author portrait"></div><div><h4>Dolor nunc vulputateulr ips consec.</h4><p>Dodfh dnec semp efhrtet lacin iate.</p><time>- 20 March, 2015</time></div></div>
<aside class="services-box abs">
  <h3>OUR SERVICES</h3>
  <ul><li>Audio Visual Production</li><li>Disk Jockys &amp; Emcees</li><li>Events Lighting</li><li>Event Planning</li><li>Videography Services</li></ul>
</aside>

<section class="events-section abs"></section>
<svg class="abs" style="left:93px;top:985px" width="16" height="16"><circle cx="8" cy="8" r="7" fill="none" stroke="#3a1c0f" stroke-width="1.3"/><path d="M9.5 5L6.5 8l3 3" stroke="#3a1c0f" stroke-width="1.3" fill="none"/></svg>
<svg class="abs" style="left:582px;top:985px" width="16" height="16"><circle cx="8" cy="8" r="7" fill="none" stroke="#2a140a" stroke-width="1.3"/><path d="M6.5 5l3 3-3 3" stroke="#2a140a" stroke-width="1.3" fill="none"/></svg>
<h2 class="events-title abs">UPCOMING EVENTS</h2>
<div class="events-rule abs"></div>
<article class="event abs" style="left:96px"><div class="cal"><span>31</span></div><h4>Dolor nunc vulepu</h4><div class="month">MARCH, 2015</div><p>Aliquam dapibus tincidunt metus. Praesent justo dolor, lobortis quis, lobortis dignissim, pulvinar ac, lorem.</p><a class="btn">READ MORE</a></article>
<article class="event abs" style="left:274px"><div class="cal"><span>25</span></div><h4>Dolor nunc vulepu</h4><div class="month">MARCH, 2015</div><p>Aliquam dapibus tincidunt metus. Praesent justo dolor, lobortis quis, lobortis dignissim, pulvinar ac, lorem.</p><a class="btn is-hot">READ MORE</a></article>
<article class="event abs" style="left:448px"><div class="cal"><span>16</span></div><h4>Dolor nunc vulepu</h4><div class="month">MARCH, 2015</div><p>Aliquam dapibus tincidunt metus. Praesent justo dolor, lobortis quis, lobortis dignissim, pulvinar ac, lorem.</p><a class="btn">READ MORE</a></article>

<footer class="site-footer abs"></footer>
<div class="social abs"><i></i><i></i><i></i><i></i></div>
<p class="copyright abs">© 2015 <b>Vorquin Events</b> LLC. All Rights Reserved. Privacy Policy.</p>
</body>
</html>
```